Come as U R - mental health service LGBTIQ inclusive poster

We are a mental health organisation in Australia that is looking for a poster design that we can put in our waiting rooms to show that our service is inclusive of gender diverse, intersex, and sexuality diverse people. We will add text and our company logo afterwards. An example has been provided for inspiration. Designers 25 and under encouraged.

Target Market(s)

Target audience - all genders 12-25.

Industry/Entity Type

Mental Health

Requirements
Must have
• This graphic should be colourful, include the text "Come as U R", and incorporate the colours of the pride flag. Should be a general design that is appropriate for all of the target audience.

```html
<!DOCTYPE html>
<html lang="en">
<head>
<meta charset="utf-8">
<title>Come as U R</title>
<link href="https://fonts.googleapis.com/css2?family=Jost:wght@200&display=swap" rel="stylesheet">
<style>
  :root {
    --teal: #6fa6b6;
    --teal-deep: #78a9b9;
    --lavender: #a59cc8;
    --mauve: #b7a2c6;
    --mint: #a3d0a0;
    --slate-blue: #8a9dc8;
    --figure-tint: #a9c6b4;
    --heart-pink: #efdcf2;
    --heart-sky: #bfe6ee;
    --heart-lime: #e6efce;
    --type: #ffffff;
  }
  html, body {
    margin: 0;
    padding: 0;
    overflow: hidden;
  }
  .poster {
    position: relative;
    width: 849px;
    height: 1200px;
    overflow: hidden;
    background: linear-gradient(180deg, #76a5b3 0%, #6ea7b6 60%, #73aec0 100%);
    font-family: "Jost", "Helvetica Neue", Arial, sans-serif;
  }
  .poster__shapes {
    position: absolute;
    inset: 0;
  }
  .poster__headline {
    position: absolute;
    left: 0;
    width: 100%;
    margin: 0;
    color: var(--type);
    font-weight: 200;
    font-size: 152px;
    line-height: 1;
    text-align: center;
    white-space: nowrap;
  }
  .poster__headline--top {
    top: 538px;
    letter-spacing: 2px;
    left: -4px;
  }
  .poster__headline--bottom {
    top: 712px;
    letter-spacing: 90px;
    left: 28px;
  }
</style>
</head>
<body>
<main class="poster">
  <svg class="poster__shapes" width="849" height="1200" viewBox="0 0 849 1200" aria-hidden="false">
    <defs>
      <linearGradient id="heart-fill" x1="0" y1="0" x2="1" y2="1">
        <stop offset="0" stop-color="var(--heart-pink)"/>
        <stop offset="0.5" stop-color="var(--heart-sky)"/>
        <stop offset="1" stop-color="var(--heart-lime)"/>
      </linearGradient>
      <linearGradient id="mint-band" x1="0" y1="0" x2="0" y2="1">
        <stop offset="0" stop-color="#a9c5a8"/>
        <stop offset="0.6" stop-color="var(--mint)"/>
        <stop offset="1" stop-color="#b3b8bb"/>
      </linearGradient>
    </defs>

    <!-- large mauve shard across the top -->
    <polygon class="shape shape--mauve" points="0,210 185,70 460,0 560,0 849,190 849,600 0,520" fill="var(--mauve)" opacity="0.55"/>
    <!-- slate-blue shard on the right -->
    <polygon class="shape shape--slate" points="560,340 849,260 849,600 440,600" fill="var(--slate-blue)" opacity="0.45"/>
    <!-- mint band through the middle -->
    <polygon class="shape shape--mint" points="0,300 185,330 690,345 600,480 849,595 849,1030 0,690" fill="url(#mint-band)" opacity="0.85"/>
    <!-- lavender chevron lower left -->
    <polygon class="shape shape--lavender" points="0,690 280,810 150,1200 0,1200 0,1120 60,940 0,760" fill="var(--lavender)" opacity="0.75"/>
    <!-- blue wedge lower right -->
    <polygon class="shape shape--blue" points="849,1040 760,1200 849,1200" fill="#7a96c0" opacity="0.8"/>

    <!-- lower-right puzzle motif -->
    <rect class="motif motif--puzzle" role="img" aria-label="Large translucent puzzle piece shape"
          x="510" y="850" width="339" height="350" rx="40" fill="#9a9ccc" opacity="0.7"/>

    <!-- people pictograms -->
    <rect class="motif motif--family" role="img" aria-label="Faint pictogram of a family walking together"
          x="100" y="395" width="125" height="120" rx="10" fill="var(--figure-tint)" opacity="0.6"/>
    <rect class="motif motif--carer" role="img" aria-label="Faint pictogram of a person pushing a wheelchair user"
          x="640" y="402" width="108" height="105" rx="10" fill="#9fb9b6" opacity="0.6"/>

    <!-- heart -->
    <path class="heart" d="M425,162 C455,95 520,70 595,72 C665,75 695,135 688,210 C675,320 520,380 425,500 C330,380 175,320 162,210 C155,135 185,75 255,72 C330,70 395,95 425,162 Z"
          fill="url(#heart-fill)" opacity="0.92"/>
  </svg>

  <h1 class="poster__headline poster__headline--top">COME AS</h1>
  <p class="poster__headline poster__headline--bottom">UR</p>
</main>
</body>
</html>
```